Flooring Company Stationery Design Project

I need Business card, presentation folder, letterhead and envelope design.
I want the design to show a lot of creativity and that it has a modern look but still professional.
The company has a retail store but we specialize in in-home shopping.

Design must have a "flooring" company style. Creativity is going to be the main thing we'll be looking for. We want something that will stand out of the competition.

We are a remodeling busines and we want to look like one but with a good look.

PLEASE USE FOLLOWING LINK FOR ANY PHOTOS NEEDED
http://www.velmorick.com/syndicate/logos/choose_brands.html
Updates

PLEASE USE ANY PHOTOS NEEDED FROM HERE

Target Market(s)

Our target customer are 35-50 years old and decision makers are usually women

Industry/Entity Type

Retail

Requirements
Must have
• Color red
PHOTOS NEEDED CAN BE USED FROM HERE

```html
<!DOCTYPE html>
<html lang="en">
<head>
<meta charset="utf-8">
<title>Floorcrest Business Cards</title>
<link rel="stylesheet" href="https://fonts.googleapis.com/css2?family=Poppins:wght@400;500;600;700&display=swap">
<style>
  :root {
    --brand-red: #c8182a;
    --brand-orange: #f2a516;
    --teal: #13818f;
    --band-brown: #b27644;
    --band-brown-light: #cf9663;
    --line-teal: #4aa7b3;
    --room-cream: #efe3c8;
    --room-warm: #d8b98c;
    --floor-brown: #7a4a28;
    --text-dark: #333333;
    --white: #ffffff;
    --backdrop: #e4e2df;
  }
  * { box-sizing: border-box; margin: 0; padding: 0; }
  html, body { width: 1200px; height: 735px; overflow: hidden; }
  body {
    background: var(--backdrop);
    font-family: "Poppins", Arial, sans-serif;
    position: relative;
  }
  .card {
    position: absolute;
    width: 514px;
    height: 294px;
    overflow: hidden;
    box-shadow: 0 2px 8px rgba(0,0,0,.18);
  }
  .card--front  { left: 64px;  top: 44px; }
  .card--plain  { left: 624px; top: 51px; background: var(--white); }
  .card--panel  { left: 66px;  top: 381px; }
  .card--dark   { left: 633px; top: 378px; }

  .room-photo {
    position: absolute; inset: 0;
    background:
      linear-gradient(180deg, var(--room-cream) 0%, var(--room-warm) 52%, #a06a3e 70%, var(--floor-brown) 100%);
  }
  .room-photo--faded::after {
    content: ""; position: absolute; inset: 0;
    background: rgba(255,255,255,.62);
  }
  .room-photo--dim::after {
    content: ""; position: absolute; inset: 0;
    background: rgba(20,14,8,.45);
  }

  .wordmark {
    position: absolute;
    display: flex; align-items: center; gap: 8px;
    font-weight: 700;
    color: var(--brand-red);
    letter-spacing: -1px;
    line-height: 1;
  }
  .wordmark__mark {
    width: 12px; height: 12px; background: var(--brand-orange);
  }
  .tagline {
    position: absolute;
    font-weight: 600;
    color: var(--teal);
    white-space: nowrap;
  }

  /* front card */
  .card--front .wordmark { left: 90px; top: 72px; font-size: 42px; }
  .card--front .tagline  { left: 268px; top: 112px; font-size: 11px; }
  .contact-band {
    position: absolute; left: 0; right: 0; top: 160px; height: 116px;
    background: linear-gradient(90deg, var(--band-brown) 0%, var(--band-brown-light) 60%, var(--band-brown) 100%);
    border-top: 2px solid var(--line-teal);
    border-bottom: 2px solid var(--line-teal);
    color: var(--white);
  }
  .person {
    position: absolute; right: 282px; top: 12px;
    text-align: right; font-size: 13px; line-height: 21px;
  }
  .person__name { font-size: 18px; font-weight: 700; line-height: 24px; }
  .contact-band__divider {
    position: absolute; left: 243px; top: 14px; width: 1px; height: 82px;
    background: rgba(255,255,255,.7);
  }
  .contact-list {
    position: absolute; left: 258px; top: 14px;
    list-style: none; font-size: 13.5px; line-height: 21px;
  }
  .contact-list li { display: flex; align-items: center; gap: 7px; }
  .contact-list svg { width: 11px; height: 11px; fill: var(--white); flex: none; }

  /* plain card */
  .card--plain .wordmark { left: 52px; top: 112px; font-size: 56px; }
  .card--plain .tagline  { left: 265px; top: 168px; font-size: 14px; }
  .web-address {
    position: absolute; left: 0; right: 0; text-align: center;
    font-weight: 500; font-size: 22px;
  }
  .card--plain .web-address { top: 252px; color: var(--text-dark); }

  /* panel card */
  .logo-panel {
    position: absolute; left: 72px; top: 96px; width: 384px; height: 96px;
    background: rgba(255,255,255,.92);
    box-shadow: 0 0 18px 12px rgba(255,255,255,.8);
  }
  .card--panel .wordmark { left: 92px; top: 136px; font-size: 42px; }
  .card--panel .tagline  { left: 266px; top: 177px; font-size: 11.5px; }
  .card--panel .web-address,
  .card--dark .web-address { top: 254px; color: var(--white); }

  /* dark card */
  .card--dark .wordmark { left: 48px; top: 120px; font-size: 54px; }
  .card--dark .tagline  { left: 258px; top: 164px; font-size: 13px; }
</style>
</head>
<body>

  <section class="card card--front">
    <div class="room-photo room-photo--faded" role="img" aria-label="Bright living room interior with tall arched windows and a polished wood floor"></div>
    <div class="wordmark"><span>floorcrest</span><span class="wordmark__mark"></span></div>
    <div class="tagline">Adding Value To Your Home</div>
    <div class="contact-band">
      <div class="person">
        <div class="person__name">Your Name</div>
        <div>Title</div>
        <div>00, Complex name</div>
        <div>City, State 0042</div>
      </div>
      <div class="contact-band__divider"></div>
      <ul class="contact-list">
        <li><svg viewBox="0 0 12 12"><path d="M2.5 1l2 2-1 1.5a6 6 0 0 0 4 4l1.5-1 2 2-1.5 1.5C5 11 1 7 1 2.5z"/></svg>0987 654321</li>
        <li><svg viewBox="0 0 12 12"><path d="M3.5 0.5h5a1 1 0 0 1 1 1v9a1 1 0 0 1-1 1h-5a1 1 0 0 1-1-1v-9a1 1 0 0 1 1-1zm0.5 1.5v7h4v-7z"/></svg>0987 654321</li>
        <li><svg viewBox="0 0 12 12"><path d="M1 2.5h10v7H1zm1 1v.3l4 2.7 4-2.7v-.3z"/></svg>info@floorcrest.com</li>
        <li><svg viewBox="0 0 12 12"><path d="M6 1a5 5 0 1 0 0 10A5 5 0 0 0 6 1zm0 1c.6 0 1.3 1.5 1.4 3.5H4.6C4.7 3.5 5.4 2 6 2zM2.1 5.5a4 4 0 0 1 1.8-3A8 8 0 0 0 3.6 5.5zm0 1h1.5a8 8 0 0 0 .3 3 4 4 0 0 1-1.8-3zm2.5 0h2.8C7.3 8.5 6.6 10 6 10s-1.3-1.5-1.4-3.5zm3.8 0h1.5a4 4 0 0 1-1.8 3 8 8 0 0 0 .3-3zm0-1a8 8 0 0 0-.3-3 4 4 0 0 1 1.8 3z"/></svg>www.floorcrest.com</li>
      </ul>
    </div>
  </section>

  <section class="card card--plain">
    <div class="wordmark"><span>floorcrest</span><span class="wordmark__mark"></span></div>
    <div class="tagline">Adding Value To Your Home</div>
    <div class="web-address">www.floorcrest.com</div>
  </section>

  <section class="card card--panel">
    <div class="room-photo" role="img" aria-label="Elegant living room with chandelier, arched windows, sofas and hardwood floor"></div>
    <div class="logo-panel"></div>
    <div class="wordmark"><span>floorcrest</span><span class="wordmark__mark"></span></div>
    <div class="tagline">Adding Value To Your Home</div>
    <div class="web-address">www.floorcrest.com</div>
  </section>

  <section class="card card--dark">
    <div class="room-photo room-photo--dim" role="img" aria-label="Dimmed living room interior with chandelier, arched windows and hardwood floor"></div>
    <div class="wordmark"><span>floorcrest</span><span class="wordmark__mark"></span></div>
    <div class="tagline">Adding Value To Your Home</div>
    <div class="web-address">www.floorcrest.com</div>
  </section>

</body>
</html>
```